PSD for Magento Site (No Code Required)

I Need 10 pages design for a new Plus-Size Lingerie Site. The site has to be a edgy, fun & clean.

I will need versions of each page for mobile, tablet sizes as well. We are trying to be a new kind of lingerie site. something non traditional. A Fun place to show. Big images, Easy Navigation, Simple Layout.

Full Brief is Attached.

Target Market(s)

Plus size Women, Lingerie Enthusiasts

Industry/Entity Type

Retail

Number of Pages Required

5+ page

Font styles to use
Sans Serif

Colors
000000
ffffff
d3d3d3

Requirements
Must have
• Well Structured Mobile versions of each page
Should not have
• clutter

```html
<!DOCTYPE html>
<html lang="en">
<head>
<meta charset="utf-8">
<title>Fullbloom Lingerie</title>
<link href="https://fonts.googleapis.com/css2?family=Lato:wght@300;400;700&family=Playball&display=swap" rel="stylesheet">
<style>
:root{
  --ink:#222;
  --muted:#555;
  --orange:#f0a045;
  --dark:#2b2526;
  --line:#e2e2e2;
  --card:#efefef;
  --white:#fff;
}
*{margin:0;padding:0;box-sizing:border-box}
html,body{width:718px;height:1200px;overflow:hidden;background:var(--white)}
body{position:relative;font-family:'Lato',sans-serif;color:var(--ink)}
.abs{position:absolute}
.logo{left:66px;top:20px;font-size:20px;font-weight:700;letter-spacing:0.5px;color:var(--ink)}
.logo-sub{left:74px;top:43px;font-size:6px;letter-spacing:12px;color:var(--ink)}
.search{left:273px;top:23px;width:190px;height:27px;border:1px solid #ccc}
.search span{position:absolute;left:9px;top:9px;font-size:6px;color:#999}
.search-btn{position:absolute;right:-1px;top:-1px;width:28px;height:27px;background:var(--ink)}
.acct-text,.cart-text{font-size:6.5px;line-height:9px}
.acct-text b,.cart-text b{font-weight:700}
.header-rule{left:0;top:67px;width:718px;height:1px;background:var(--line)}
.nav{left:0;top:83px;width:718px;font-size:7px;color:#444}
.nav span{position:absolute;top:0;white-space:nowrap}
.nav .active{color:var(--orange)}
.nav-rule{left:0;top:105px;width:718px;height:1px;background:var(--line)}
.hero{left:0;top:106px;width:718px;height:311px;background:linear-gradient(90deg,#efefef,#dcdcdc)}
.hero-photo{left:360px;top:106px;width:260px;height:311px;background:linear-gradient(180deg,#c9a28c,#b9a5a2 50%,#d6d2d0)}
.dropdown{left:259px;top:105px;width:99px;height:65px;background:#231f20;color:#ddd;font-size:6.5px;z-index:2}
.dropdown span{position:absolute;left:17px}
.hero-kicker{left:117px;top:168px;font-size:9px;color:var(--ink)}
.hero-script1{left:106px;top:176px;font-family:'Playball',cursive;font-size:44px;color:var(--ink)}
.hero-script2{left:104px;top:220px;font-family:'Playball',cursive;font-size:68px;color:var(--ink)}
.hero-sub{left:117px;top:313px;font-size:11.5px;color:var(--ink)}
.dot{top:398px;width:6px;height:6px;border-radius:50%;background:#aaa}
.dot.on{background:var(--orange)}
.banner{top:442px;width:186px;height:168px;border:2px solid #ddd}
.banner-title{font-family:'Playball',cursive;color:var(--white);font-size:24px;line-height:26px}
.shop-btn{border:1px solid var(--white);color:var(--white);font-size:7px;padding:8px 13px}
.tabs{top:639px;font-size:8.5px;color:#444}
.tab-line{left:173px;top:653px;width:44px;height:2px;background:var(--orange)}
.card{top:675px;width:136px;height:240px;background:var(--card)}
.card-img{position:absolute;left:3px;top:2px;width:130px;height:153px}
.card-name{position:absolute;left:13px;top:169px;font-size:7.5px;color:#333}
.card-desc{position:absolute;left:13px;top:181px;font-size:6px;line-height:12.5px;color:#555;width:115px}
.card-price{position:absolute;left:13px;top:207px;font-size:16px;color:#333}
.add-cart{position:absolute;left:3px;top:97px;width:130px;height:30px;background:var(--orange);color:var(--white);font-size:7px;text-align:center;line-height:30px}
.wishlist{position:absolute;left:3px;top:127px;width:130px;height:28px;background:#231f20;color:var(--white);font-size:6.5px;text-align:center;line-height:28px}
.news{left:0;top:947px;width:718px;height:57px;background:var(--dark)}
.news-label{left:98px;top:968px;font-size:12px;color:var(--white)}
.news-input{left:187px;top:960px;width:228px;height:30px;background:var(--white)}
.news-input span{position:absolute;left:12px;top:11px;font-size:6.5px;color:#888}
.news-btn{position:absolute;left:194px;top:4px;width:27px;height:22px;background:var(--orange)}
.follow{left:462px;top:968px;font-size:12px;color:var(--white)}
.social{top:970px;width:10px;height:10px;border-radius:50%;background:var(--white)}
.social.on{background:var(--orange)}
.foot-head{top:1026px;font-size:9px;color:#333}
.foot-links{top:1046px;font-size:7px;color:#444;line-height:18.5px}
.foot-rule{top:1027px;width:1px;height:103px;background:var(--line)}
.contact-text{left:466px;top:1046px;font-size:6.5px;color:#777;line-height:15px}
.circle{left:466px;width:25px;height:25px;border-radius:50%;background:var(--orange)}
.contact-line{left:498px;font-size:9px;color:#333}
.bottom{left:0;top:1154px;width:718px;height:46px;background:var(--dark)}
.bottom-text{top:1172px;font-size:6.5px;color:#ddd}
</style>
</head>
<body>
<!-- header -->
<div class="abs logo">FULLBLOOM</div>
<div class="abs logo-sub">LINGERIE</div>
<div class="abs search"><span>Search...</span>
  <div class="search-btn"><svg width="28" height="27"><circle cx="13" cy="12.5" r="3" fill="none" stroke="#fff" stroke-width="1.3"/><line x1="15.2" y1="14.7" x2="17.5" y2="17" stroke="#fff" stroke-width="1.3"/></svg></div>
</div>
<svg class="abs" style="left:477px;top:27px" width="16" height="18"><circle cx="8" cy="5" r="4" fill="#222"/><path d="M1 17 Q1 10 8 10 Q15 10 15 17Z" fill="#222"/></svg>
<div class="abs acct-text" style="left:499px;top:28px"><b>MY ACCOUNT</b><br>LOGIN/REGISTER</div>
<div class="abs" style="left:566px;top:22px;width:1px;height:28px;background:#ddd"></div>
<svg class="abs" style="left:579px;top:29px" width="18" height="16"><path d="M1 2h3l2 8h9l2-6H5" fill="none" stroke="#222" stroke-width="2"/><circle cx="7" cy="13.5" r="1.6" fill="#222"/><circle cx="14" cy="13.5" r="1.6" fill="#222"/></svg>
<div class="abs cart-text" style="left:603px;top:28px"><b>MY CART</b><br>0 ITEM(S)-$0.00</div>
<div class="abs header-rule"></div>

<!-- navigation -->
<div class="abs nav">
  <span class="active" style="left:69px">LINGERIE</span>
  <span style="left:118px">COSTUMES</span>
  <span style="left:173px">PANTIES</span>
  <span style="left:217px">DRESSES</span>
  <span style="left:263px;color:#111">SLEEPWEAR</span>
  <span style="left:321px">HOSIERY</span>
  <span style="left:368px">ACCESSORIES</span>
  <span style="left:431px">PVC/LEATHER</span>
  <span style="left:495px">HOLIDAY COLLECTION</span>
  <span style="left:587px">SALE &amp; CLEARANCE</span>
</div>
<div class="abs nav-rule"></div>

<!-- hero -->
<div class="abs hero"></div>
<div class="abs hero-photo" role="img" aria-label="Model in a blush plus-size bodysuit posing with hands on hips"></div>
<div class="abs dropdown">
  <span style="top:9px">ROBES</span>
  <span style="top:27px">CHEMISES</span>
  <span style="top:45px">CAMISOLES &amp; SETS</span>
</div>
<div class="abs hero-kicker">A diverse variety of</div>
<div class="abs hero-script1">Glamorous</div>
<div class="abs hero-script2">High</div>
<div class="abs hero-sub">quality plus size lingerie</div>
<div class="abs dot" style="left:335px"></div>
<div class="abs dot" style="left:345px"></div>
<div class="abs dot on" style="left:356px"></div>
<div class="abs dot" style="left:366px"></div>
<div class="abs dot" style="left:376px"></div>

<!-- promo banners -->
<div class="abs banner" style="left:66px;background:linear-gradient(160deg,#8fa9b8,#5a6a5c 60%,#3b6f78)" role="img" aria-label="Model in teal babydoll on a palm-lined beach">
  <div class="abs banner-title" style="left:18px;top:100px">Exclusive<br>Collection</div>
</div>
<div class="abs banner" style="left:266px;background:linear-gradient(160deg,#4a4440,#2a2624 60%,#1e1b1a)" role="img" aria-label="Model in black lace lingerie by a window">
  <div class="abs banner-title" style="left:18px;top:20px;font-size:26px;line-height:28px">Sexy<br>Lingerie</div>
  <div class="abs" style="left:18px;top:80px;font-size:6px;color:#eee;line-height:15px">Lorem ipsum dolor sit amet, consectetur<br>adipiscing elit. Praesent ut urna.</div>
  <div class="abs shop-btn" style="left:20px;top:120px">SHOP NOW</div>
</div>
<div class="abs banner" style="left:466px;background:linear-gradient(160deg,#5a4a2c,#3a2e26 55%,#6b5a4a)" role="img" aria-label="Model in floral kimono and black lace with warm bokeh lights">
  <div class="abs banner-title" style="left:18px;top:96px">Clearance<br>&nbsp;-50%</div>
</div>

<!-- tabs -->
<div class="abs tabs" style="left:173px;color:#111">POPULAR</div>
<div class="abs tabs" style="left:270px">NEW ARRIVALS</div>
<div class="abs tabs" style="left:390px">BEST SELLERS</div>
<div class="abs tabs" style="left:503px">SPECIALS</div>
<div class="abs tab-line"></div>

<!-- products -->
<div class="abs card" style="left:66px">
  <div class="card-img" style="background:linear-gradient(180deg,#8aa4b4,#3a3a36 60%,#6a6058)" role="img" aria-label="Model in black corset with garters"></div>
  <div class="card-name">CORSET</div>
  <div class="card-desc">Lorem ipsum dolor sit amet, conse ctetur adipiscing rhoncus.</div>
  <div class="card-price">$ 25.00</div>
</div>
<div class="abs card" style="left:215px">
  <div class="card-img" style="background:linear-gradient(180deg,#4a5a3e,#2a2624 60%,#1e1b1a)" role="img" aria-label="Model in black bustier"></div>
  <div class="add-cart">&#x1F6D2;&#xFE0E; ADD TO CART</div>
  <div class="wishlist">&#9825; ADD TO WISHLIST</div>
  <div class="card-name">BUSTIER</div>
  <div class="card-desc">Lorem ipsum dolor sit amet, conse ctetur adipiscing rhoncus.</div>
  <div class="card-price">$ 37.00</div>
</div>
<div class="abs card" style="left:365px">
  <div class="card-img" style="background:linear-gradient(180deg,#eeeeee,#8a8480 55%,#2a2624)" role="img" aria-label="Model in black lace chemise"></div>
  <div class="card-name">CHEMISE</div>
  <div class="card-desc">Lorem ipsum dolor sit amet, conse ctetur adipiscing rhoncus.</div>
  <div class="card-price">$ 41.00</div>
</div>
<div class="abs card" style="left:515px">
  <div class="card-img" style="background:linear-gradient(180deg,#3c6a8a,#3a3aa0 55%,#4a5a66)" role="img" aria-label="Model in blue babydoll and g-string"></div>
  <div class="card-name">BABYDOLL &amp; G-STRING</div>
  <div class="card-desc">Lorem ipsum dolor sit amet, conse ctetur adipiscing rhoncus.</div>
  <div class="card-price">$ 25.00</div>
</div>

<!-- newsletter -->
<div class="abs news"></div>
<div class="abs news-label">NEWSLETTER</div>
<div class="abs news-input"><span>Email Address</span>
  <div class="news-btn"><svg width="27" height="22"><path d="M8 11h10M14 7l4 4-4 4" fill="none" stroke="#fff" stroke-width="2"/></svg></div>
</div>
<div class="abs follow">FOLLOW US</div>
<div class="abs social" style="left:548px"></div>
<div class="abs social on" style="left:566px"></div>
<div class="abs social" style="left:587px"></div>
<div class="abs social" style="left:609px"></div>

<!-- footer -->
<div class="abs foot-head" style="left:66px">SUPPORT</div>
<div class="abs foot-links" style="left:66px">CONTACT US<br>SIZING CHART<br>FAQ<br>SHIPPING<br>RETURNS</div>
<div class="abs foot-rule" style="left:159px"></div>
<div class="abs foot-head" style="left:194px">POPULAR LINKS</div>
<div class="abs foot-links" style="left:194px">LOVE HURTS<br>FANTASY LEAGUE<br>TOPS<br>SKIRTS<br>SWIMSUITS</div>
<div class="abs foot-rule" style="left:302px"></div>
<div class="abs foot-head" style="left:338px">QUICK LINKS</div>
<div class="abs foot-links" style="left:338px">LINGERIE<br>COSTUMES<br>PANTIES<br>DRESSES<br>SLEEPWEAR</div>
<div class="abs foot-rule" style="left:430px"></div>
<div class="abs foot-head" style="left:466px">CONTACT</div>
<div class="abs contact-text">Lorem ipsum dolor sit amet, consectetur adipiscing elit.<br>Praesent ut urna at justo tristique viverra</div>
<div class="abs circle" style="top:1077px"><svg width="25" height="25"><path d="M9 8c1 0 1.5 2.5 1 3-.5.4-.7.8 0 1.8s1.6 1.8 2.4 2c.6 0 1-.8 1.5-1 .6 0 2.6 1 2.5 1.6 0 1-1.3 1.8-2.4 1.6C11 16.5 8.5 14 8 10.5 7.8 9 8.2 8 9 8z" fill="#fff"/></svg></div>
<div class="abs contact-line" style="top:1084px">123 456 789 00000</div>
<div class="abs circle" style="top:1108px"><svg width="25" height="25"><rect x="7.5" y="9" width="10" height="7" fill="#fff"/><path d="M7.5 9l5 4 5-4" fill="none" stroke="#f0a045" stroke-width="1"/></svg></div>
<div class="abs contact-line" style="top:1115px">info@domainname.com</div>

<!-- bottom bar -->
<div class="abs bottom"></div>
<div class="abs bottom-text" style="left:66px">Privacy Policy &nbsp;|&nbsp; Sitemap</div>
<div class="abs bottom-text" style="left:456px">Copyright@2016 FULLBLOOM LINGERIE. All Right Reserved.</div>
</body>
</html>
```